Full Website and E-Commerce Design. New Business. Selling digital downloads related to the call cen

I am planning to launch a new online company called maplequartzservices.com. This will be a place where people who work in call centres can come and purchase downloadable templates, tool-kits, courseware etc to help them in their jobs. The site will also share the latest information around research, best practices, news in the industry. Essentially a hub for Maple Quartz Services related.

I need someone to build the site for me from scratch (I have only just bought the domain name). Everything from the look and feel of the website (focus on easy to use, clean and sharp graphics, with a bit of fun), highly focused on social media and building a community, full blown e-commerce that allows for memberships/subscriptions/and one off purchase models. If you can also design custom graphics (high quality) that would be even better. Given my research of other companies in this space their websites are very dull that look like knowledge bases. I will want alot of cool visuals that attract the customers in. My initial thinking on colour scheme is bright greens/pinks/yellows etc. Not fluorescent though!

The site will contain alot of documents, templates, presentations, videos, articles, white papers etc. You must have experience in the best way to structure the site in an organised manner so that my customer can find what they need very easily.

The person who takes on this work must be happy to work collaboratively with me. It is also key that when the project is delivered that I am able to maintain alot of it myself in terms of uploading documents, blog updates, adding new products, real-time reports/analytics etc.

Whilst you are designing the website I will be working on the content so I will need your help to understand how I structure my content so that it makes sense for the design.

I will base my choice of designer on levels of experience (I will want to see previous work that you have done). I am not adverse to you using tools like shopify etc. if it meets the overall requirements of the site and adds to the functionality/look and feel.

Target Market(s)

People who work in call centres primarily those that are responsible for managing teams of the call centre itself

Industry/Entity Type

Business

Number of Pages Required

5+ page

Font styles to use
Sans Serif

Colors
33b8a4
34a6d7
886aae
b868aa
e667a6
f04a51
f68e4e
faa54b
ffcf3e

Requirements
Must have
• E-commerce functionality that allows for subscriptions and one-off payments
• Credit card processing and accept wire/bank transfers
• Easy to use layout
• Products sold alone and/or as part of bundles
• Membership area
• Front page
• About Us page
• Contact Us page
• Store page (with e-commerce back end)
• News page
• Free Resources page
• Cool, bright, fun look and feel
Nice to have
• Cool, bright, fun graphics
Should not have
• Should not look old fashioned or be difficult to navigate
• Should not look too busy or disorganised

```html
<!DOCTYPE html>
<html lang="en">
<head>
<meta charset="utf-8">
<title>Maple Quartz Services</title>
<link rel="stylesheet" href="https://fonts.googleapis.com/css2?family=Raleway:wght@400;500;700&family=Open+Sans:wght@400&display=swap">
<style>
  :root {
    --header-top: #14a7dc;
    --header-bottom: #0a82c6;
    --white: #ffffff;
    --page-bg: #ffffff;
    --panel-border: #c9c9c9;
    --panel-head: #f1f1f1;
    --link-text: #555555;
    --chevron: #a5a5a5;
    --footer-bg: #e9e9e9;
    --footer-text: #5c5c5c;
    --social-ring: #555555;
  }
  * { box-sizing: border-box; margin: 0; padding: 0; }
  html, body { width: 1200px; height: 860px; overflow: hidden; background: var(--page-bg); }
  body { position: relative; font-family: "Raleway", sans-serif; }

  .site-header {
    position: absolute; left: 0; top: 0; width: 1200px; height: 105px;
    background: linear-gradient(180deg, var(--header-top), var(--header-bottom));
  }
  .brand {
    position: absolute; left: 183px; top: 36px;
    font-family: "Raleway", sans-serif; font-weight: 500; font-size: 24px;
    color: var(--white); letter-spacing: 0.3px;
  }
  .main-nav { position: absolute; top: 44px; left: 0; }
  .main-nav a {
    position: absolute; white-space: nowrap; color: var(--white);
    font-size: 15px; font-weight: 500; text-decoration: none;
  }

  .quick-links {
    position: absolute; left: 182px; top: 132px; width: 184px; height: 243px;
    border: 1px solid var(--panel-border);
  }
  .quick-links h2 {
    height: 35px; line-height: 35px; padding-left: 20px;
    background: var(--panel-head); border-bottom: 1px solid var(--panel-border);
    font-family: "Raleway", sans-serif; font-weight: 400; font-size: 16px; color: #444;
  }
  .quick-links ul { list-style: none; padding-top: 10px; }
  .quick-links li {
    position: relative; height: 26.4px; line-height: 26.4px; padding-left: 25px;
    font-family: "Open Sans", sans-serif; font-size: 11px; color: var(--link-text);
  }
  .quick-links li::after {
    content: ""; position: absolute; right: 18px; top: 10px;
    width: 6px; height: 6px; border-top: 1px solid var(--chevron); border-right: 1px solid var(--chevron);
    transform: rotate(45deg);
  }

  .tile {
    position: absolute; width: 201px; height: 184px; color: var(--white);
  }
  .tile::before {
    content: ""; position: absolute; inset: 8px 9px;
    border: 1px solid rgba(255,255,255,0.85);
  }
  .tile-icon { position: absolute; left: 50%; top: 30px; transform: translateX(-50%); }
  .tile-title {
    position: absolute; left: 0; right: 0; text-align: center;
    font-weight: 700; font-size: 14.5px; line-height: 22px; text-transform: uppercase;
  }
  .icon-spot {
    position: absolute; left: 50%; top: 28px; width: 62px; height: 62px; transform: translateX(-50%);
    border-radius: 8px; background: rgba(255,255,255,0.28);
  }

  .tile--performance { left: 385px; top: 132px; background: radial-gradient(circle, #a2e21e, #6cc20b); }
  .tile--morale { left: 601px; top: 132px; background: radial-gradient(circle, #c17fe0, #9944c2); }
  .tile--coaching { left: 817px; top: 132px; background: radial-gradient(circle, #ffbc20, #ff9800); }
  .tile--leadership { left: 385px; top: 324px; background: radial-gradient(circle, #ffe600, #ffc10c); }
  .tile--reward { left: 601px; top: 324px; background: radial-gradient(circle, #2c93bd, #13638d); }
  .tile--communication { left: 817px; top: 324px; background: radial-gradient(circle, #1ad4e6, #04adcb); }
  .tile--technology { left: 386px; top: 516px; background: radial-gradient(circle, #ec4ca2, #cf2f70); }
  .tile--strategy { left: 603px; top: 516px; background: radial-gradient(circle, #26d6fb, #00b4ee); }
  .tile--research { left: 818px; top: 516px; background: radial-gradient(circle, #cde225, #a5c70e); }

  .site-footer {
    position: absolute; left: 0; top: 753px; width: 1200px; height: 107px; background: var(--footer-bg);
  }
  .footer-nav a {
    position: absolute; top: 29px; white-space: nowrap;
    font-family: "Open Sans", sans-serif; font-size: 13px; color: var(--footer-text); text-decoration: none;
  }
  .copyright {
    position: absolute; left: 185px; top: 57px;
    font-family: "Open Sans", sans-serif; font-size: 11px; color: var(--footer-text);
  }
  .social { position: absolute; left: 905px; top: 28px; display: flex; gap: 2px; }
  .social a {
    display: block; width: 27px; height: 27px; border-radius: 50%;
    border: 1.5px solid var(--social-ring);
  }
</style>
</head>
<body>
  <header class="site-header">
    <div class="brand">Maple Quartz Services</div>
    <nav class="main-nav">
      <a href="#" style="left:492px">About Us</a>
      <a href="#" style="left:598px">News</a>
      <a href="#" style="left:678px">Free Stuff</a>
      <a href="#" style="left:787px">Membership</a>
      <a href="#" style="left:916px">Contact Us</a>
    </nav>
  </header>

  <aside class="quick-links">
    <h2>Quick Links</h2>
    <ul>
      <li>At ac mi quis</li>
      <li>Lacus mollis</li>
      <li>Aliquam Curabitur</li>
      <li>Tempus eros Curabitur</li>
      <li>Vel mi sit amet</li>
      <li>Magna malesuada</li>
      <li>Rltrices Utnisi</li>
    </ul>
  </aside>

  <main>
    <a class="tile tile--performance">
      <svg class="tile-icon" width="56" height="52" viewBox="0 0 56 52" fill="none" stroke="#fff" stroke-width="2">
        <rect x="1" y="1" width="54" height="48" rx="3"/>
        <line x1="1" y1="11" x2="55" y2="11"/>
        <circle cx="7" cy="6" r="1.3" fill="#fff"/><circle cx="12" cy="6" r="1.3" fill="#fff"/><circle cx="17" cy="6" r="1.3" fill="#fff"/>
        <path d="M16 38 A12 12 0 0 1 40 38"/>
        <line x1="28" y1="38" x2="35" y2="28"/>
        <circle cx="28" cy="38" r="2.5"/>
      </svg>
      <div class="tile-title" style="top:111px">Performance<br>Measurement &amp;<br>Management</div>
    </a>

    <a class="tile tile--morale">
      <div class="icon-spot" role="img" aria-label="Icon of a person with a lightbulb idea"></div>
      <div class="tile-title" style="top:126px">Morale and<br>Motivation</div>
    </a>

    <a class="tile tile--coaching">
      <div class="icon-spot" role="img" aria-label="Icon of a coach presenting to a small group"></div>
      <div class="tile-title" style="top:126px">Coaching and<br>Mentoring</div>
    </a>

    <a class="tile tile--leadership">
      <div class="icon-spot" style="top:38px" role="img" aria-label="Icon of a team of people"></div>
      <div class="tile-title" style="top:119px; font-size:16px; line-height:19px">Leadership and<br>Management</div>
    </a>

    <a class="tile tile--reward">
      <svg class="tile-icon" style="top:36px" width="46" height="66" viewBox="0 0 46 66" fill="#fff">
        <path d="M23 2 l5 4 6-1 2 6 6 3-1 6 3 5-3 5 1 6-6 3-2 6-6-1-5 4-5-4-6 1-2-6-6-3 1-6-3-5 3-5-1-6 6-3 2-6 6 1z"/>
        <circle cx="23" cy="23" r="11" fill="#1a75a0"/>
        <circle cx="23" cy="23" r="7" fill="#fff"/>
        <circle cx="23" cy="23" r="4.5" fill="#1a75a0"/>
        <path d="M13 40 L5 60 L13 56 L17 64 L22 46z"/>
        <path d="M33 40 L41 60 L33 56 L29 64 L24 46z"/>
      </svg>
      <div class="tile-title" style="top:121px">Reward and<br>Recognition</div>
    </a>

    <a class="tile tile--communication">
      <svg class="tile-icon" style="top:54px" width="48" height="40" viewBox="0 0 48 40" fill="none" stroke="#fff" stroke-width="3.5">
        <path d="M20 3 C9 3 2 9 2 16 c0 4 2 7 5 9 l-2 7 8-5 c2 .5 4 .8 7 .8 c11 0 18-6 18-12 S31 3 20 3z"/>
        <path d="M38 15 c5 2 8 6 8 10 c0 3-1.5 5-4 7 l1 6-6-4 c-2 .5-3.5 .5-5 .5 c-5 0-9-2-11-5"/>
      </svg>
      <div class="tile-title" style="top:121px">Communication<br>Skills</div>
    </a>

    <a class="tile tile--technology">
      <svg class="tile-icon" style="top:36px" width="70" height="70" viewBox="0 0 70 70" fill="none" stroke="#fff" stroke-width="2">
        <path d="M10 38 V30 C10 14 21 4 35 4 S60 14 60 30 V38"/>
        <path d="M14 30 C14 17 23 8 35 8 S56 17 56 30"/>
        <rect x="4" y="36" width="10" height="20" rx="4"/>
        <rect x="56" y="36" width="10" height="20" rx="4"/>
        <path d="M60 56 C60 64 52 67 40 67"/>
        <rect x="28" y="64" width="14" height="5" rx="2.5"/>
      </svg>
      <div class="tile-title" style="top:124px">Call Centre<br>Technology</div>
    </a>

    <a class="tile tile--strategy">
      <div class="icon-spot" style="top:34px; width:72px; height:70px" role="img" aria-label="Icon of a presenter beside a strategy flow chart"></div>
      <div class="tile-title" style="top:124px">Call Centre<br>Strategy</div>
    </a>

    <a class="tile tile--research">
      <svg class="tile-icon" style="top:48px" width="64" height="44" viewBox="0 0 64 44" fill="none" stroke="#fff" stroke-width="3">
        <rect x="9" y="2" width="46" height="32" rx="3"/>
        <path d="M1 39 H63 V41 H1z" fill="#fff"/>
      </svg>
      <div class="tile-title" style="top:124px">Research and<br>Best Practices</div>
    </a>
  </main>

  <footer class="site-footer">
    <nav class="footer-nav">
      <a href="#" style="left:185px">About Us</a>
      <a href="#" style="left:265px">News</a>
      <a href="#" style="left:325px">Free Stuff</a>
      <a href="#" style="left:408px">Membership</a>
      <a href="#" style="left:508px">Contact Us</a>
    </nav>
    <p class="copyright">© 2015 Company Name&nbsp; All right reserved&nbsp; Term of Use</p>
    <div class="social">
      <a href="#" aria-label="Social profile 1"></a>
      <a href="#" aria-label="Social profile 2"></a>
      <a href="#" aria-label="Social profile 3"></a>
      <a href="#" aria-label="Social profile 4"></a>
    </div>
  </footer>
</body>
</html>
```